Real Estate Agent Service Brochure

I need a trifold brochure to showcase my real estate services. I am a veteran Real Estate Broker specializing in marketing properties for sale and for top dollar. I would like to see designs that use colors from my logo (attached) and I would like to showcase some before and after photos of staging jobs I have done to homes to get them ready for the market. This brochure is specific to home sellers. You are happy to go check out my website for inspiration www.lomavertpa.com but keep the copy as I have written it. The the final design should communicate experienced professional who uses current technologies and strategies to market properties for the highest value.

Target Market(s)

Homeowners wanting to sell their homes

Industry/Entity Type

Real Estate Agent

Font styles to use
Serif

Requirements
Must have
• My, logo, personal photo, title and contact information as listed:
• Marta Venholt
• Owner Broker
• Stager Re-Designer
• 860-912-7048
• BRAVE Realty LLC
• LOMAVERTPA.com
• Marta@LOMAVERTPA.com
• The colors used should be those in my logo.
• Brochure should be able to fit in standard envelope for mailing.
Nice to have
• I think I would like my personal photo and contact information on the front panel.
Should not have
• Bright colors.

```html
<!DOCTYPE html>
<html lang="en">
<head>
<meta charset="utf-8">
<title>BRAVE Realty LLC – Seller Brochure</title>
<link href="https://fonts.googleapis.com/css2?family=Roboto+Condensed:wght@300;400&family=Montserrat:ital,wght@1,300;1,400&family=Lora:wght@400&family=Great+Vibes&display=swap" rel="stylesheet">
<style>
:root{
  --navy:#14164a;
  --navy-deep:#0f1140;
  --paper:#ffffff;
  --mist:#d9d9d9;
  --mist-light:#e6e6e6;
  --ink:#2a2a3a;
  --ink-soft:#6b6b78;
  --ink-faint:#9a9aa4;
  --bg-top:#f2f3f7;
  --bg-bottom:#b9bfd3;
}
*{margin:0;padding:0;box-sizing:border-box}
html,body{width:1200px;height:1200px;overflow:hidden}
body{background:linear-gradient(180deg,var(--bg-top),var(--bg-bottom));position:relative;font-family:"Roboto Condensed",sans-serif;color:var(--ink)}
.sheet{position:absolute;left:239px;width:709px;height:552px;background:var(--navy);box-shadow:0 4px 14px rgba(20,22,74,.18)}
.sheet--outside{top:42px}
.sheet--inside{top:619px}
.abs{position:absolute}
.photo{position:absolute}
.body-copy{font-size:10px;line-height:12.6px;font-weight:300;color:var(--ink-soft);text-align:justify;text-indent:6px}
.quote{position:absolute;font-family:"Montserrat",sans-serif;font-style:italic;font-weight:300;font-size:7.4px;line-height:10.5px;color:var(--navy);text-align:justify}
.quote--faint{color:var(--ink-faint)}
.quote::before{content:"\201C";position:absolute;left:-9px;top:-6px;font-family:Georgia,serif;font-style:normal;font-weight:700;font-size:16px;color:var(--navy)}
.quote__by{display:block;text-align:right;border-top:1px solid var(--navy);margin-top:2px;padding-top:1px;font-style:normal}
.quote__by::after{content:" \201D";font-family:Georgia,serif;font-weight:700;font-size:12px}
.brand{font-family:"Lora",serif;color:var(--navy);display:flex;align-items:center;gap:5px}
.brand__mark{width:8px;height:8px;background:var(--navy)}
.contact{position:absolute;left:722px;display:flex;align-items:center;gap:6px;font-family:"Lora",serif;font-size:6.6px;color:var(--ink);white-space:nowrap}
.contact svg{width:14px;height:14px;flex:none}
.signature{position:absolute;left:724px;top:446px;font-family:'Great Vibes',cursive;font-size:15px;color:var(--ink-soft);white-space:nowrap}
.portrait{position:absolute;left:824px;top:440px;width:117px;height:146px;border-radius:14px;background:linear-gradient(180deg,#6a4a34,#3a2a22 60%,#1b1b22)}
</style>
</head>
<body>

<div class="sheet sheet--outside"></div>

<section class="about-panel abs" style="left:255px;top:58px;width:228px;height:520px;background:var(--paper);overflow:hidden">
  <div class="abs" style="right:0;top:0;width:42px;height:140px;background:var(--mist-light)"></div>
  <svg class="abs" style="left:0;top:337px" width="228" height="183" role="img" aria-label="Photo of polished hardwood floor in a staged room">
    <defs><linearGradient id="wood" x1="0" x2="1"><stop offset="0" stop-color="#7a4a2a"/><stop offset="1" stop-color="#c58a55"/></linearGradient></defs>
    <path d="M0 0 C20 100 90 160 160 183 L0 183 Z" fill="url(#wood)"/>
  </svg>
  <p class="body-copy abs" style="left:15px;top:12px;width:191px">A veteran in the real estate industry with nearly 30 years expertise and consistent membership in the Multi-Million-Dollar Club combined with her Certified Home Stager and Re-Designer credentials assures that her clients get the advantage of vast knowledge, seasoned experience and proven results, all geared to creating beautiful spaces, which form a connection with the right buyer producing the highest and best offer.</p>
  <p class="body-copy abs" style="left:15px;top:161px;width:191px">Marta devotes her efforts to selling real estate, by keeping up with the evolving market, researching buyer trends and preparing homes before they enter the market by staging them to connect with the target buyer. Marta knows all sales are not alike. Therefore, taking a cookie cutter approach is not acceptable, she recognizes that each property is unique and requires a personalized marketing plan and strategy.</p>
  <div class="abs" style="left:93px;top:307px;width:43px;height:43px;background:var(--navy)">
    <svg width="43" height="43" viewBox="0 0 43 43" fill="none" stroke="#fff" stroke-width="1.4"><path d="M13 13V30H31"/><path d="M15 27L20 21L24 24L30 16"/></svg>
  </div>
  <h3 class="abs" style="left:0;width:220px;top:358px;text-align:center;font-family:'Lora',serif;font-weight:400;font-size:12px;color:var(--ink)">Proven Market Knowledge</h3>
  <p class="body-copy abs" style="left:18px;top:390px;width:188px;color:var(--ink);font-size:9.8px;text-indent:0">That's what you can expect when you work with seasoned specialist Marta Venholt for all your Real Estate needs. The sale of a home is too important an undertaking to entrust to just anyone. Select a dedicated, service-oriented and results-driven broker who understands the intricacies of the Real Estate process... <span style="display:block;text-align:center">select Marta.</span></p>
</section>

<svg class="abs" style="left:483px;top:58px" width="450" height="520">
  <rect width="450" height="520" fill="var(--navy)"/>
  <rect x="233" width="217" height="520" fill="var(--navy-deep)"/>
  <polygon points="0,275 233,382 450,235 450,520 233,520 0,520" fill="var(--mist-light)"/>
  <polygon points="233,382 450,235 450,520 233,520" fill="var(--paper)"/>
</svg>

<div class="photo" style="left:585px;top:58px;width:348px;height:235px;border-bottom-left-radius:135px 235px;background:linear-gradient(135deg,#f2e8d8,#b58750 55%,#4a3220)" role="img" aria-label="Staged kitchen and dining area with chandelier"></div>

<div class="abs" style="left:483px;top:518px;width:233px;text-align:center">
  <div class="brand" style="justify-content:center;font-size:20px"><span class="brand__mark"></span>BRAVE</div>
  <div style="font-family:'Lora',serif;font-size:11px;color:var(--ink-soft);margin-top:4px">BRAVE Realty LLC</div>
</div>

<div class="brand abs" style="left:820px;top:380px;font-size:28px;font-weight:400;letter-spacing:1px"><span class="brand__mark"></span>BRAVE</div>
<div class="abs" style="left:852px;top:410px;font-family:'Lora',serif;font-size:6px;letter-spacing:3px;color:var(--navy)">REALTY LLC</div>

<div class="portrait" role="img" aria-label="Portrait of Marta Venholt, owner broker"></div>

<div class="signature">Marta Venholt</div>
<div class="abs" style="left:727px;top:472px;font-family:'Lora',serif;font-size:8px;color:var(--ink)">OWNER BROKER</div>

<div class="contact" style="top:501px"><svg viewBox="0 0 15 15" fill="none" stroke="var(--ink)"><circle cx="7.5" cy="7.5" r="6.8"/><path d="M5 4.5l1.5 1.6-.8 1.2c.5 1 1.2 1.7 2.2 2.2l1.2-.8 1.6 1.5-1 1c-2.8-.4-5.2-2.8-5.6-5.6z" fill="var(--ink)" stroke="none"/></svg>860-912-7048</div>
<div class="contact" style="top:523px"><svg viewBox="0 0 15 15" fill="none" stroke="var(--ink)"><circle cx="7.5" cy="7.5" r="6.8"/><rect x="4" y="5" width="7" height="5"/><path d="M4 5l3.5 3L11 5"/></svg>marta@lomavertpa.com</div>
<div class="contact" style="top:545px"><svg viewBox="0 0 15 15" fill="none" stroke="var(--ink)"><circle cx="7.5" cy="7.5" r="6.8"/><circle cx="7.5" cy="7.5" r="3.5"/><path d="M4 7.5h7M7.5 4v7"/></svg>www.lomavertpa.com</div>

<div class="sheet sheet--inside"></div>

<section class="abs" style="left:255px;top:635px;width:225px;height:520px;background:var(--paper);overflow:hidden">
  <div class="abs" style="left:150px;top:145px;width:130px;height:400px;border-top-left-radius:130px 260px;background:var(--mist-light)"></div>
  <div class="photo" style="left:0;top:0;width:225px;height:146px;background:linear-gradient(135deg,#e9e6e2,#a19a92 55%,#3d3028)" role="img" aria-label="Staged open-plan dining room"></div>
  <div class="photo" style="left:123px;top:117px;width:102px;height:70px;border:2px solid #f3d8b8;background:linear-gradient(135deg,#d8d2cc,#4a3a30)" role="img" aria-label="Hallway with hardwood floors"></div>
  <h2 class="abs" style="left:6px;top:163px;font-family:'Roboto Condensed',sans-serif;font-weight:300;font-size:22.5px;line-height:27px;color:var(--ink-faint)">This is what<br>Marta's clients says<br>about their experiences:</h2>
  <p class="quote" style="left:12px;top:264px;width:193px">In the Real Estate Business there are many, but none like Marta. She brings a level of professionalism far above other Brokers. She will have no trouble selling your house. What is different is her honesty, sincerity, and unquestionable ethics. She will make sure that you are satisfied with every aspect of your transaction.<span class="quote__by">Walter G</span></p>
  <p class="quote quote--faint" style="left:12px;top:390px;width:193px">Marta and the team at Brave are knowledgeable and professional. I have been involved in three separate real estate transactions with Marta as my broker. I am always pleased and impressed by her negotiating skills, her market knowledge and her ability to manage the process.<span class="quote__by" style="margin-top:8px">Denise T</span></p>
</section>

<section class="abs" style="left:480px;top:635px;width:236px;height:520px;background:var(--mist-light);overflow:hidden">
  <div class="abs" style="left:-30px;top:0;width:280px;height:220px;border-top-left-radius:260px 60px;background:var(--paper)"></div>
  <div class="abs" style="left:32px;top:13px;font-family:'Montserrat',sans-serif;font-size:11px;color:var(--navy)">Harriet L</div>
  <p class="quote" style="left:20px;top:28px;width:193px">Am so glad that we found Marta to help us in staging a property that we had just finished renovating. She listened to our ideas of what we envisioned in the spaces based on the style of the house and put it all together and on time for the first open house that got rave reviews! Her combined background in real estate and interior design made her a perfect partner for our job.<span class="quote__by" style="border:0">Harriet L</span></p>
  <p class="quote quote--faint" style="left:20px;top:149px;width:193px">The marketing and staging of our house was on point. I don't think the sale of our home would have been as successful without it.<span class="quote__by">Paul &amp; Irene S</span></p>
  <div class="photo" style="left:130px;top:200px;width:103px;height:87px;background:linear-gradient(135deg,#e6d2b8,#7a5a3e)" role="img" aria-label="Living room with fireplace"></div>
  <div class="photo" style="left:28px;top:226px;width:102px;height:154px;background:linear-gradient(135deg,#f1efe9,#8d857a)" role="img" aria-label="Bright family room with large windows"></div>
  <div class="photo" style="left:90px;top:287px;width:143px;height:93px;background:linear-gradient(135deg,#e4ddd2,#6e5a48)" role="img" aria-label="Staged living room with stone fireplace"></div>
  <p class="quote" style="left:20px;top:393px;width:193px">I have had several real estate dealings with Marta each one was handled professionally and with my best interest in mind. Her marketing skills are top notch she made sure my properties where ready for market and showcased them in the best way by staging them and having professional photography done. She helped me get through home inspections issues keeping the sales in tact. I keep using her services and recommend her to family and friends she really knows her stuff!<span class="quote__by" style="margin-top:4px">Yvonne K</span></p>
</section>

<section class="abs" style="left:716px;top:635px;width:217px;height:520px;background:var(--mist-light);overflow:hidden">
  <p class="quote quote--faint" style="left:15px;top:20px;width:195px">Marta worked with our builder to help us design new floor plans, she was responsible for all the selections/finishes and then completely staged and decorated the homes using some furniture from old models and also shopping for new furniture. The model homes came out beautiful! The feedback was amazing and all the homes sold quickly! She was responsible with updates and reports. We will be using her services again for our next project!<span class="quote__by" style="border-color:var(--ink-faint)">Curtis H</span></p>
  <div class="photo" style="left:132px;top:138px;width:85px;height:62px;background:linear-gradient(135deg,#e8e3db,#5c4838)" role="img" aria-label="Empty room with chandelier before staging"></div>
  <div class="photo" style="left:5px;top:167px;width:127px;height:93px;background:linear-gradient(135deg,#d7d0c8,#6a5c52)" role="img" aria-label="Staged bedroom with neutral bedding"></div>
  <p class="quote" style="left:15px;top:276px;width:195px">Marta directed us right from the beginning by preparing a market evaluation using current data, helping us to establish a proper list price; she prepared our property for the market by staging it and then marketed it with great photography and video tours. Because of her pre-marketing preparations we received several offers on our house! Keeping our interests first, Marta negotiated the best deal for us; we were truly blown away by her knowledge, work ethic and professionalism.<span class="quote__by" style="margin-left:30px">Ray &amp; Lena W</span></p>
  <div class="photo" style="left:5px;top:400px;width:88px;height:88px;background:linear-gradient(135deg,#cfc8c0,#4a3c32)" role="img" aria-label="Bedroom before staging"></div>
  <div class="photo" style="left:76px;top:427px;width:141px;height:93px;background:linear-gradient(135deg,#ece6de,#7a6656)" role="img" aria-label="Bedroom after staging"></div>
</section>

</body>
</html>
```